Require Digital Banner Ads for a startup Travel Booking SIte

Vaylo is the brand name of a travel booking site. The site features properties only in Pakistan. The site is set to go Live in first week of November and for this we plan to run a branding Campaign targeted at raising awareness about the brand and its USPs. This campaign will be run on QRN and on ZP Display.
At the same time we will also be using our ZP and Pixo pages.
We require Ad and Social media Post designs for this campaign.
Site: vaylo.pk
ZP page: https://www.zapnest.com/VayloPK/

Target Market(s)

Middle and high income group males & females- single and with families - interest in travel, photography, adventure, food
Business Traveler looking looking for flexibility in accommodation choices when traveling for work
Youth budget traveler looking for deals
Family traveler
frequent travelers
Inbound International travelers

Industry/Entity Type

Travel Industry

Colors

Designer to choose colors to be used in the design.

Requirements
Must have
• Vaylo Logo
• We need to develop 4 themes to cover the 4 messages
• 1. Vaylo is a travel booking site where people can book accommodation online for Pakistan
• 2. We have a large variety of pre qualified properties. this means that our reps have gone and actually seen the properties and you will get what you see online ,
• 3. Safe and secure payment
• 4. Secure booking with live CC to help sort out issues
Nice to have
• we can share pictures and images and videos. pls develop design using sample imagery
• Ads should try and capture peoples attention based on why people travel:
• To be known
• to explore
• to meet new people
• to relax
• improve lifestyle
Should not have
• nudity
• explicit language or imagery
• sexual imagery or language
• religious affiliation
• ethnic affinity

```html
<!DOCTYPE html>
<html lang="en">
<head>
<meta charset="utf-8">
<title>Vaylo – Display Banner Set</title>
<link rel="stylesheet" href="https://fonts.googleapis.com/css2?family=Raleway:wght@300;400;700;800&display=swap">
<style>
  :root {
    --frame: #333333;
    --plum: #3d2f56;
    --plum-text: #5a1f6b;
    --orange: #f05a28;
    --coral: #e8452c;
    --maroon: #5c0a2b;
    --white: #ffffff;
    --ink: #4a2b55;
  }
  * { box-sizing: border-box; margin: 0; padding: 0; }
  html, body { width: 1200px; height: 624px; overflow: hidden; background: var(--frame); }
  body { font-family: "Raleway", sans-serif; position: relative; }

  .banner { position: absolute; width: 576px; height: 301px; overflow: hidden; }
  .banner--discover { left: 19px; top: 6px; }
  .banner--relax { left: 605px; top: 6px; }
  .banner--secure { left: 19px; top: 316px; }
  .banner--support { left: 605px; top: 316px; }

  .banner svg.shapes { position: absolute; inset: 0; width: 100%; height: 100%; }
  .photo { position: absolute; inset: 0; }

  .photo--laptop {
    background:
      radial-gradient(ellipse 190px 120px at 420px 110px, rgba(236,238,242,0.95), rgba(236,238,242,0) 100%),
      radial-gradient(ellipse 170px 70px at 400px 230px, rgba(70,70,78,0.85), rgba(70,70,78,0) 100%),
      radial-gradient(ellipse 140px 90px at 560px 290px, rgba(232,128,70,0.9), rgba(232,128,70,0) 100%),
      radial-gradient(ellipse 120px 80px at 240px 170px, rgba(228,128,70,0.7), rgba(228,128,70,0) 100%),
      linear-gradient(120deg, #9a8a8e 0%, #bca7a2 40%, #cdb2a8 70%, #c7a296 100%);
  }
  .photo--patio {
    background:
      radial-gradient(ellipse 120px 150px at 130px 150px, rgba(110,30,80,0.9), rgba(110,30,80,0) 100%),
      radial-gradient(ellipse 200px 110px at 420px 90px, rgba(232,214,178,0.95), rgba(232,214,178,0) 100%),
      radial-gradient(ellipse 180px 70px at 240px 190px, rgba(170,140,110,0.8), rgba(170,140,110,0) 100%),
      radial-gradient(ellipse 110px 80px at 80px 270px, rgba(35,40,55,0.95), rgba(35,40,55,0) 100%),
      linear-gradient(180deg, #1f3f9a 0%, #23408a 35%, #4a5a6e 65%, #6b5a4d 100%);
  }
  .photo--mountain {
    background:
      radial-gradient(ellipse 280px 60px at 230px 140px, rgba(212,206,200,0.9), rgba(212,206,200,0) 100%),
      radial-gradient(ellipse 300px 40px at 200px 200px, rgba(125,105,72,0.85), rgba(125,105,72,0) 100%),
      radial-gradient(ellipse 40px 60px at 290px 180px, rgba(30,30,34,0.8), rgba(30,30,34,0) 100%),
      linear-gradient(180deg, #e3e8ee 0%, #ccd3da 28%, #b8b0a6 48%, #8f7e62 66%, #8a8a86 80%, #6d6e6c 100%);
  }
  .photo--reception {
    background:
      radial-gradient(ellipse 120px 130px at 290px 180px, rgba(190,50,50,0.95), rgba(190,50,50,0) 100%),
      radial-gradient(ellipse 110px 90px at 440px 70px, rgba(120,60,50,0.85), rgba(120,60,50,0) 100%),
      radial-gradient(ellipse 90px 140px at 545px 170px, rgba(225,210,200,0.9), rgba(225,210,200,0) 100%),
      radial-gradient(ellipse 120px 70px at 450px 250px, rgba(45,30,30,0.85), rgba(45,30,30,0) 100%),
      radial-gradient(ellipse 130px 90px at 70px 260px, rgba(110,80,65,0.9), rgba(110,80,65,0) 100%),
      linear-gradient(110deg, #7a5a48 0%, #9a4a3c 45%, #7a4c40 72%, #b99a88 100%);
  }

  .brand {
    position: absolute;
    font-family: "Raleway", sans-serif;
    font-weight: 800;
    line-height: 1;
    letter-spacing: 0.5px;
  }
  .tag { position: absolute; text-transform: uppercase; line-height: 1.25; }
  .tag strong { font-weight: 700; }
  .cta { position: absolute; font-weight: 700; text-transform: uppercase; }

  /* Discover */
  .banner--discover .brand { left: 0; width: 230px; top: 58px; text-align: center; color: var(--white); font-size: 40px; }
  .banner--discover .tag { left: 0; width: 230px; top: 124px; text-align: center; color: var(--white); font-weight: 300; font-size: 11.5px; line-height: 1.22; }
  .banner--discover .cta { left: 0; width: 230px; top: 179px; text-align: center; color: var(--white); font-size: 11.5px; }

  /* Relax */
  .banner--relax .brand { left: 340px; width: 232px; top: 144px; text-align: center; color: var(--coral); font-size: 48px; }
  .banner--relax .tag { left: 334px; width: 240px; top: 218px; text-align: center; color: var(--plum-text); font-weight: 300; font-size: 10.5px; line-height: 1.3; }
  .banner--relax .cta { left: 340px; width: 232px; top: 259px; text-align: center; color: var(--plum-text); font-size: 11.5px; }

  /* Secure */
  .banner--secure .brand { right: 22px; top: 86px; color: var(--white); font-size: 40px; }
  .banner--secure .tag { right: 22px; top: 150px; text-align: right; font-size: 11.5px; line-height: 1.22; }
  .banner--secure .tag .lead { color: var(--plum-text); font-weight: 700; display: block; }
  .banner--secure .tag .rest { color: var(--plum-text); font-weight: 300; display: block; }
  .banner--secure .rule { position: absolute; right: 22px; top: 215px; width: 103px; height: 1px; background: var(--maroon); opacity: 0.6; }
  .banner--secure .cta { right: 22px; top: 227px; color: var(--white); font-size: 11.5px; }
  .secure-badge { position: absolute; right: 22px; top: 264px; display: flex; align-items: center; gap: 4px; }
  .secure-badge span { font-size: 7.5px; line-height: 1.05; text-transform: uppercase; color: var(--plum-text); }
  .secure-badge strong { font-weight: 700; font-size: 8.5px; display: block; }

  /* Support */
  .banner--support .brand { left: 0; width: 220px; top: 24px; text-align: center; color: var(--coral); font-size: 44px; }
  .banner--support .tag { left: 0; width: 224px; top: 92px; text-align: center; color: var(--ink); font-weight: 300; font-size: 8px; line-height: 1.35; }
  .banner--support .cta { left: 0; width: 224px; top: 126px; text-align: center; color: var(--plum-text); font-size: 11.5px; text-transform: none; }
  .banner--support .agent {
    position: absolute; left: 65px; top: 148px; width: 92px; height: 92px; border-radius: 50%;
    border: 3px solid rgba(255,255,255,0.6);
    background:
      radial-gradient(circle at 50% 40%, #e9d3c0 0%, #d8b996 30%, rgba(216,185,150,0) 55%),
      linear-gradient(180deg, #b9c8d8 0%, #9fb2c8 60%, #6f8aa8 100%);
  }
</style>
</head>
<body>

<section class="banner banner--discover">
  <div class="photo photo--laptop" role="img" aria-label="Photo of a person on a sofa browsing travel destinations on a laptop"></div>
  <svg class="shapes" viewBox="0 0 576 301" aria-hidden="true">
    <polygon points="0,0 178,0 275,301 0,301" fill="#c9bfca" opacity="0.6"/>
    <polygon points="0,0 168,0 262,301 0,301" fill="var(--plum)" opacity="0.93"/>
  </svg>
  <div class="brand">Vaylo</div>
  <p class="tag">Your new<br>travel companion</p>
  <p class="cta">Find great places</p>
</section>

<section class="banner banner--relax">
  <div class="photo photo--patio" role="img" aria-label="Photo of a cheerful woman on an evening patio with a tablet showing the same patio"></div>
  <svg class="shapes" viewBox="0 0 576 301" aria-hidden="true">
    <polygon points="168,301 576,20 576,301" fill="var(--white)"/>
    <polygon points="468,85 576,22 576,142" fill="var(--maroon)"/>
  </svg>
  <div class="brand">Vaylo</div>
  <p class="tag">If you want to <strong>relax on this patio,</strong><br>Vaylo will take you there</p>
  <p class="cta">Find great places</p>
</section>

<section class="banner banner--secure">
  <div class="photo photo--mountain" role="img" aria-label="Photo of a traveller standing before snowy mountains reflected in a lake"></div>
  <svg class="shapes" viewBox="0 0 576 301" aria-hidden="true">
    <polygon points="455,0 576,0 576,301 365,301" fill="#9aa0ad"/>
    <polygon points="461,0 576,0 576,301 372,301" fill="var(--orange)"/>
  </svg>
  <div class="brand">Vaylo</div>
  <p class="tag"><span class="lead">Simplify<br>your travel</span><span class="rest">Prepay for your<br>accommodation</span></p>
  <div class="rule"></div>
  <p class="cta">Find great places</p>
  <div class="secure-badge">
    <svg width="13" height="18" viewBox="0 0 13 18" aria-hidden="true">
      <path d="M3 8V5a3.5 3.5 0 0 1 7 0v3" fill="none" stroke="var(--plum-text)" stroke-width="1.8"/>
      <rect x="0.5" y="8" width="12" height="9.5" rx="1.2" fill="var(--plum-text)"/>
      <path d="M3.5 12.5l2 2 4-4" fill="none" stroke="var(--orange)" stroke-width="1.4"/>
    </svg>
    <span><strong>Secure</strong>Payment</span>
  </div>
</section>

<section class="banner banner--support">
  <div class="photo photo--reception" role="img" aria-label="Photo of a smiling family checking in at a hotel reception desk"></div>
  <svg class="shapes" viewBox="0 0 576 301" aria-hidden="true">
    <polygon points="0,0 220,0 225,168 0,168" fill="var(--white)" opacity="0.88"/>
  </svg>
  <div class="brand">Vaylo</div>
  <p class="tag">All you need to do is show up.<br><strong>Your booking is guaranteed</strong> with Vaylo</p>
  <p class="cta">Find Great Places</p>
  <div class="agent" role="img" aria-label="Photo of a customer support agent wearing a headset"></div>
</section>

</body>
</html>
```